New Business Cards for KM&DR

We need updated business cards for a staff of 15 engineers, estimators, project managers, and sales people. We have recently begun changes to our website and marketing material to improve our look and branding. We are an established fabricator specializing in pressure vessels, tanks, and structural steel. The owners require us to use the existing logo and old english text design. Also, we prefer dark grey or mostly black cards.
Target Market(s)
Engineers, purchasing agents, estimators, and project managers of; mining companies, refineries, industrial construction professionals
Industry/Entity Type
Business
Contact Information for Business Card
Logo, phone, website, email, etc.
Look and feel
Each slider illustrates characteristics of the customer's brand and the style your logo design should communicate.

```html
<!DOCTYPE html>
<html lang="en">
<head>
<meta charset="utf-8">
<title>KM&amp;DR Business Cards</title>
<link rel="stylesheet" href="https://fonts.googleapis.com/css2?family=Oswald:wght@500;700&family=Work+Sans:wght@400;500&display=swap">
<style>
  :root {
    --backdrop: #2b2320;
    --card-black: #0b0b0b;
    --card-white: #ffffff;
    --ink: #111111;
    --ink-soft: #3a3a3a;
    --silver: #cfcfcf;
    --silver-soft: #8c8c8c;
  }
  * { box-sizing: border-box; margin: 0; padding: 0; }
  html, body {
    width: 1200px; height: 715px; overflow: hidden;
    background: var(--backdrop);
  }
  .canvas {
    position: relative; width: 1200px; height: 715px;
    display: flex; align-items: center; justify-content: center; gap: 50px;
  }
  .card {
    width: 520px; height: 300px; border-radius: 14px;
    position: relative; overflow: hidden;
    box-shadow: 0 18px 40px rgba(0,0,0,.45);
  }
  .card--front {
    background: var(--card-black);
    display: flex; align-items: center; justify-content: center;
  }
  .front-mark {
    display: flex; flex-direction: column; align-items: center; gap: 10px;
    color: var(--silver);
  }
  .front-mark__name {
    display: flex; align-items: center; gap: 12px;
    font-family: "Oswald", sans-serif; font-weight: 700;
    font-size: 44px; letter-spacing: 3px;
  }
  .front-mark__square {
    width: 16px; height: 16px; background: var(--silver);
  }
  .front-mark__year {
    font-family: "Work Sans", sans-serif; font-size: 15px;
    letter-spacing: 6px; color: var(--silver-soft);
  }
  .card--back {
    background: var(--card-white); color: var(--ink);
    display: flex; align-items: center;
  }
  .badge {
    width: 50%; display: flex; flex-direction: column; align-items: center;
    font-family: "Oswald", sans-serif; font-weight: 700; color: var(--ink);
  }
  .badge__count { font-size: 26px; line-height: 1; }
  .badge__name { font-size: 38px; letter-spacing: 2px; line-height: 1.2; }
  .badge__year { font-family: "Work Sans", sans-serif; font-weight: 500; font-size: 13px; letter-spacing: 4px; }
  .badge__label { font-size: 24px; letter-spacing: 1px; margin-top: 4px; }
  .divider {
    width: 1.5px; height: 150px; background: var(--ink);
  }
  .contact {
    padding-left: 24px; font-family: "Work Sans", sans-serif;
    font-size: 14px; line-height: 1.32; color: var(--ink-soft);
  }
  .contact__name {
    font-family: "Oswald", sans-serif; font-weight: 700;
    font-size: 30px; letter-spacing: .5px; color: var(--ink); line-height: 1.05;
  }
  .contact__role { font-size: 12px; letter-spacing: 1px; margin-bottom: 6px; }
  .contact__row { display: flex; align-items: center; gap: 8px; }
  .contact__row svg { width: 10px; height: 10px; fill: var(--ink); flex: none; }
  .contact__address { margin-bottom: 2px; }
</style>
</head>
<body>
<main class="canvas">
  <section class="card card--front" aria-label="Card front">
    <div class="front-mark">
      <div class="front-mark__name"><span class="front-mark__square"></span>KM&amp;DR</div>
      <div class="front-mark__year">1976</div>
    </div>
  </section>

  <section class="card card--back" aria-label="Card back">
    <div class="badge">
      <div class="badge__count">40</div>
      <div class="badge__name">KM&amp;DR</div>
      <div class="badge__year">1976</div>
      <div class="badge__label">ANNIVERSARY</div>
    </div>
    <div class="divider"></div>
    <div class="contact">
      <div class="contact__name">MARCUS HALE</div>
      <div class="contact__role">DIRECTOR</div>
      <div class="contact__address">410 East 200 South<br>Granite Falls, UT 84010</div>
      <div class="contact__row">
        <svg viewBox="0 0 10 10"><path d="M2 0h2l1 3-1.5 1a6 6 0 0 0 2.5 2.5L7 5l3 1v2c0 1-1 2-2 2A8 8 0 0 1 0 2c0-1 1-2 2-2z"/></svg>
        555.014.2280
      </div>
      <div class="contact__row">
        <svg viewBox="0 0 10 10"><rect x="0" y="3" width="10" height="7" rx="1"/><rect x="2" y="0" width="6" height="3"/></svg>
        555.014.7731
      </div>
      <div class="contact__row">
        <svg viewBox="0 0 10 10"><path d="M0 2h10v6H0z M0 2l5 3.5L10 2" stroke="#fff" stroke-width=".8"/></svg>
        jordan@kmanddr.com
      </div>
      <div class="contact__row">
        <svg viewBox="0 0 10 10"><circle cx="5" cy="5" r="5"/><path d="M0 5h10M5 0v10" stroke="#fff" stroke-width=".8"/></svg>
        www.kmanddr.com
      </div>
    </div>
  </section>
</main>
</body>
</html>
```